Label design for organic saffron, saffron and herbal syrup

We cultivate saffron, Damszen roses, flowers and herbs. We would need a recognizable outfit (label) for our products. Theoretically (and practically) we have "converted" the family coat of arms into a kind of LOGO. I would send this in the attachment. It would be nice if - in one way or another - this LOGO / coat of arms could be used (certainly with other colors). For some time we have played with the idea of changing the second part of the family name "Pirnhalder" (in German .... greuth sounds similar to Kraut / herb [English]) .... eg Pirnhalder's saffron syrup into the labeling.
Our products are primarily syrups, currently herbal syrup and saffron syrup. Here the first problem arises, the only bottles / caps that are actually approved for syrup filling (hot filling) are appallingly ugly (see attachment), the only possibility of "sprucing up" is to use so-called "shrink sleeves" (here we need a diameter of 31 and a length of about 40), the colors of which are also limited. Besides the syrup, we sell saffron as a spice and various herbal mixtures (see appendix current packaging saffron). Our quantities are small (syrup 200ml-330ml), saffron in the gram range.
We also need quasi the back of the labeling (this should be able to be redefined per charge) .... Batch 1 (with small quantity has eg more of herb xy than the next batch or the saffron syrup with batch xy needs more / less saffron). In addition, we are certified organic (for this reason, the reverse side would also have to contain all the requirements of organic labeling) [see attachment].
We do not really want to address a specific clientele. Maybe just people who want to taste, enjoy, mix drinks, cook .... (and - unfortunately - don't like Quelvet syrup :-) and want to pay a bit more, or find our saffron or herbs better than others) .
In summary
- Strong recognition value (possibly inclusion of "coat of arms", color variable ... although I personally don't like yellow that much)
- Saffron syrup (the color of the saffron syrup is yellow / golden-yellow-light orange, in a transparent ugly bottle)
- Herbal syrup (color variable from blue / green / brown / red elements, in transparent ugly bottle)
Saffron and other herbs (very small containers, type of container not yet fixed)
Regarding a potential "style" I can unfortunately give little information. On the one hand, I am in love with minimalism, on the other hand, I find the translucent, cryptic, implied enormously attractive and sometimes even the "overloaded" colorful has its charm. I think that all in all, it just has to be coherent, and then it will be good.
Requirements
Must have
- Integration of Code of Arms, modifiable for different products

```html
<!DOCTYPE html>
<html lang="de">
<head>
<meta charset="utf-8">
<title>Pirnhalder's Kräuter Sirup – Etiketten</title>
<link rel="stylesheet" href="https://fonts.googleapis.com/css2?family=Ultra&family=Cinzel:wght@700;900&family=Barlow+Semi+Condensed:wght@500;600&display=swap">
<style>
  :root {
    --stage: #8c1744;
    --front-bg: #9badf2;
    --back-bg: #d9bb8c;
    --ink-blue: #3a3fb8;
    --edge-blue: #4f58cf;
    --arms-blue: #5a63cf;
    --arms-gold: #c9a46a;
    --cert-bg: #eee6d4;
    --cert-edge: #8a7f6a;
    --cert-shape: #b7ab92;
    --seal-shape: #7f88db;
    --white: #ffffff;
  }
  * { box-sizing: border-box; margin: 0; padding: 0; }
  html, body { width: 1200px; height: 675px; overflow: hidden; }
  body { background: var(--stage); position: relative; font-family: "Barlow Semi Condensed", sans-serif; }

  .label {
    position: absolute; top: 43px; width: 420px; height: 588px;
    border-radius: 12px; border: 2px solid var(--edge-blue); overflow: hidden;
    text-align: center; color: var(--ink-blue);
  }
  .label--front { left: 165px; background: var(--front-bg); }
  .label--back { left: 615px; background: var(--back-bg); }

  .arms {
    position: absolute; left: 50%; transform: translateX(-50%);
    border-radius: 40% 40% 48% 48%;
    background: radial-gradient(ellipse at 50% 60%, var(--arms-gold) 0 32%, var(--arms-blue) 60%, rgba(90,99,207,0) 72%);
  }
  .label--front .arms { top: 16px; width: 300px; height: 254px; }
  .label--back .arms { top: 14px; width: 160px; height: 144px; }

  .brand {
    position: absolute; left: 0; right: 0;
    font-family: "Cinzel", serif; font-weight: 900; letter-spacing: 1px;
    color: var(--ink-blue); line-height: 1;
  }
  .label--front .brand { top: 290px; font-size: 27px; }
  .label--back .brand { top: 172px; font-size: 25px; }

  .product {
    position: absolute; left: 0; right: 0;
    font-family: "Ultra", serif; font-weight: 400; color: var(--white); line-height: 0.9;
    letter-spacing: -1px;
    text-shadow: -1px -1px 0 var(--ink-blue), 1px -1px 0 var(--ink-blue), -1px 1px 0 var(--ink-blue), 2px 2px 0 var(--ink-blue), 4px 4px 0 var(--ink-blue);
  }
  .label--front .product { top: 322px; font-size: 84px; }
  .label--back .product { top: 200px; font-size: 56px; }

  .volume {
    position: absolute; left: 0; right: 0; top: 513px;
    font-size: 23px; font-weight: 600; line-height: 1.1;
  }
  .organic-seal { position: absolute; right: 20px; bottom: 16px; width: 80px; height: 80px; }

  .batch-info {
    position: absolute; left: 0; right: 0; top: 332px;
    font-size: 22px; font-weight: 500; line-height: 1.08;
  }
  .cert-box {
    position: absolute; left: 104px; top: 428px; width: 210px; height: 110px;
    background: var(--cert-bg); border: 1.5px solid var(--cert-edge);
  }
  .cert-mark { position: absolute; left: 8px; top: 6px; width: 100px; height: 66px; background: var(--cert-shape); }
  .cert-seal { position: absolute; right: 14px; top: 6px; width: 64px; height: 64px; border-radius: 50%; background: var(--cert-shape); }
  .cert-text {
    position: absolute; left: 8px; bottom: 4px; text-align: left;
    color: #222; font-size: 15.5px; font-weight: 500; line-height: 1;
  }
  .footnote {
    position: absolute; left: 0; right: 0; top: 550px;
    font-size: 15px; font-weight: 600; letter-spacing: 0.3px;
  }
</style>
</head>
<body>
  <section class="label label--front" aria-label="Vorderseite">
    <div class="arms" role="img" aria-label="Familienwappen mit zwei gekrönten Helmen, Blütenschild und Band"></div>
    <p class="brand">PIRNHALDER'S</p>
    <h1 class="product">Kräuter<br>Sirup</h1>
    <p class="volume">200 mL<br>1:7</p>
    <svg class="organic-seal" viewBox="0 0 80 80" role="img" aria-label="Platz für Bio-Prüfzeichen">
      <circle cx="40" cy="40" r="38" fill="var(--seal-shape)"/>
    </svg>
  </section>

  <section class="label label--back" aria-label="Rückseite">
    <div class="arms" role="img" aria-label="Familienwappen, klein"></div>
    <p class="brand">PIRNHALDER'S</p>
    <h2 class="product">Kräuter<br>Sirup</h2>
    <p class="batch-info">Zutaten: XXXXXX*<br>NAME<br>Adresse: Straße, PLZ, Ort</p>
    <div class="cert-box">
      <div class="cert-mark" role="img" aria-label="Platz für Bio-Siegel"></div>
      <div class="cert-seal" role="img" aria-label="Platz für Bio-Prüfzeichen"></div>
      <p class="cert-text">XX-ÖKO-000<br>Österreich-Landwirtschaft</p>
    </div>
    <p class="footnote">*aus kontrolliert biologischer Landwirtschaft</p>
  </section>
</body>
</html>
```